TLVinkcraft Permanent Makeup Artisan - Owner/Operator

Id like my card to present my qualitative, creative, modern & professional work in the Beauty industry. Being a male and in this line of work I need to come across as the best in my field. I am a passionate person and love what I do. I work hard, travel far, actively connect with my clients and go the extra mile. I'm associated with DermaluxClinics all over SA and my clients get refered to my via word of mouth. Doctors and other professionals in the Beauty industry talk about my qualitative work and ethics. Thus my business card needs to represent this image and standard of work.

Target Market(s)

Woman 20-70 yr old

Contact Information for Business Card

Pieter Verhoef
Permanent Makeup Artisan
+27 (0) 71 482 5093
info@TLVinkcraft.example
www.TLVinkcraft.example

Font styles to use
Other font styles liked:
• Brannball, Bell MT, Arial

Colors
feeeee

Requirements
Must have
• Small logos of the social media sites I'm visible on.
• A short discription of my experience and what I do now with the current services I offer, perhaps.
Should not have
• Look cluttered nor to much

```html
<!DOCTYPE html>
<html lang="en">
<head>
<meta charset="utf-8">
<title>TLVinkcraft Business Card</title>
<link href="https://fonts.googleapis.com/css2?family=Arimo:wght@400&display=swap" rel="stylesheet">
<style>
  :root {
    --backdrop: #2a2a2a;
    --card-white: #feeeee;
    --card-face: #ffffff;
    --teal: #5fbfbf;
    --ink: #1c1c1c;
    --icon-teal: #6fc4c4;
    --social: #8a9aa6;
    --shade-pink: #e8b4c8;
    --shade-violet: #9a6bc0;
    --shade-aqua: #7fd3d6;
    --shade-skin: #f1d9cc;
  }
  * { margin: 0; padding: 0; box-sizing: border-box; }
  html, body {
    width: 1200px; height: 997px; overflow: hidden;
    background: var(--backdrop);
    font-family: "Arimo", Arial, sans-serif;
  }
  .card {
    position: absolute; left: 280px;
    width: 640px; height: 370px;
    border-radius: 22px; overflow: hidden;
    box-shadow: 0 14px 30px rgba(0,0,0,.45);
  }
  .card-front { top: 70px; }
  .card-back { top: 520px; background: linear-gradient(135deg, var(--card-face), var(--card-white)); }

  .eye-photo {
    position: absolute; inset: 0;
    background:
      radial-gradient(ellipse 45% 30% at 50% 55%, var(--shade-violet), transparent 70%),
      linear-gradient(160deg, var(--shade-skin) 0%, var(--shade-pink) 35%, var(--shade-violet) 55%, var(--shade-aqua) 80%, var(--shade-pink) 100%);
  }

  .brand-name {
    font-family: "Arimo", Arial, sans-serif;
    font-weight: 400; color: var(--ink);
    line-height: 1; white-space: nowrap;
  }
  .front-brand { position: absolute; right: 34px; bottom: 44px; font-size: 28px; }
  .back-brand { position: absolute; left: 90px; top: 70px; font-size: 48px; }

  .rule { position: absolute; height: 1.5px; background: var(--teal); }
  .rule-top { left: 90px; right: 50px; top: 150px; }
  .rule-name { left: 300px; right: 50px; top: 228px; }

  .holder { position: absolute; left: 46px; top: 208px; }
  .holder-name { color: var(--teal); font-size: 20px; letter-spacing: .5px; text-transform: uppercase; }
  .holder-title { color: var(--ink); font-size: 15px; margin-top: 3px; }

  .contacts { position: absolute; left: 46px; top: 270px; list-style: none; }
  .contacts li { display: flex; align-items: center; gap: 16px; font-size: 16px; color: var(--ink); height: 27px; }
  .contacts svg { width: 16px; height: 16px; }

  .social { position: absolute; right: 52px; top: 195px; display: flex; gap: 8px; }
  .social span { width: 15px; height: 15px; border-radius: 50%; background: var(--social); }
</style>
</head>
<body>
  <section class="card card-front">
    <div class="eye-photo" role="img" aria-label="Close-up photograph of a made-up eye with pink, violet and aqua eyeshadow and long lashes"></div>
    <div class="brand-name front-brand">TLVinkcraft</div>
  </section>

  <section class="card card-back">
    <div class="brand-name back-brand">TLVinkcraft</div>
    <div class="rule rule-top"></div>

    <div class="holder">
      <div class="holder-name">Pieter Verhoef</div>
      <div class="holder-title">Permanent Makeup Artisan</div>
    </div>
    <div class="rule rule-name"></div>

    <div class="social" aria-label="Social media profiles">
      <span></span><span></span><span></span><span></span><span></span>
    </div>

    <ul class="contacts">
      <li>
        <svg viewBox="0 0 16 16" aria-hidden="true"><circle cx="8" cy="8" r="8" fill="var(--icon-teal)"/><path d="M5 4.5h2l.8 2-1.2.8a5 5 0 0 0 2.1 2.1l.8-1.2 2 .8v2a1 1 0 0 1-1 1A6.5 6.5 0 0 1 4 5.5a1 1 0 0 1 1-1z" fill="#fff"/></svg>
        +27 (0) 71 482 5093
      </li>
      <li>
        <svg viewBox="0 0 16 16" aria-hidden="true"><circle cx="8" cy="8" r="8" fill="var(--icon-teal)"/><rect x="4" y="5" width="8" height="6" rx="1" fill="#fff"/><path d="M4.3 5.4 8 8.3l3.7-2.9" stroke="var(--icon-teal)" stroke-width="1" fill="none"/></svg>
        info@TLVinkcraft.example
      </li>
      <li>
        <svg viewBox="0 0 16 16" aria-hidden="true"><circle cx="8" cy="8" r="8" fill="var(--icon-teal)"/><circle cx="8" cy="8" r="4" fill="none" stroke="#fff" stroke-width="1"/><path d="M4 8h8M8 4c-2 2.2-2 5.8 0 8M8 4c2 2.2 2 5.8 0 8" stroke="#fff" stroke-width="1" fill="none"/></svg>
        www.TLVinkcraft.example
      </li>
    </ul>
  </section>
</body>
</html>
```